Bramble Hollow is company name.Handknit&crochet blankets&scarves. Need logo&business ...

I need a design that is eye catching, using yarn and is flowing. I'd like to see colors in aqua (Halvorsen Pike paint HP4817 Merilune) for the yarn and company name. For the text, a dark grey color (Halvorsen Pike HP5308 Velden Ash)

Colors
87cfc7

```html
<!DOCTYPE html>
<html lang="en">
<head>
<meta charset="utf-8">
<title>Bramble Hollow – Business Card</title>
<link rel="stylesheet" href="https://fonts.googleapis.com/css2?family=Architects+Daughter&display=swap">
<style>
  :root {
    --merilune-aqua: #87cfc7;
    --velden-ash: #6a6a6a;
    --paper: #ffffff;
  }
  * { margin: 0; padding: 0; box-sizing: border-box; }
  html, body {
    width: 1200px;
    height: 1200px;
    overflow: hidden;
    background: var(--paper);
  }
  .canvas {
    position: relative;
    width: 1200px;
    height: 1200px;
    background: var(--paper);
    font-family: "Architects Daughter", cursive;
  }
  .business-card {
    position: absolute;
    left: 30px;
    top: 352px;
    width: 1140px;
    height: 602px;
    border: 2px solid var(--merilune-aqua);
    background: var(--paper);
  }
  .brand {
    position: absolute;
    left: 80px;
    top: 88px;
    display: flex;
    align-items: center;
    gap: 22px;
  }
  .brand-dot {
    width: 58px;
    height: 58px;
    border-radius: 50%;
    background: var(--merilune-aqua);
    flex: none;
  }
  .brand-name {
    font-size: 88px;
    line-height: 1;
    color: var(--merilune-aqua);
    font-weight: 400;
    letter-spacing: 1px;
  }
  .contact,
  .offerings {
    position: absolute;
    list-style: none;
    color: var(--velden-ash);
    font-size: 33px;
    line-height: 42px;
    letter-spacing: 3px;
    text-transform: uppercase;
    white-space: nowrap;
  }
  .contact {
    left: 42px;
    top: 390px;
  }
  .offerings {
    left: 658px;
    top: 370px;
  }
</style>
</head>
<body>
  <main class="canvas">
    <section class="business-card">
      <div class="brand">
        <span class="brand-dot" aria-hidden="true"></span>
        <h1 class="brand-name">Bramble Hollow</h1>
      </div>

      <ul class="contact">
        <li class="contact-name">Dana Whitlock</li>
        <li class="contact-phone">Phone#</li>
        <li class="contact-email">Email Adress</li>
      </ul>

      <ul class="offerings">
        <li>Hand Knit: Crochet</li>
        <li>Baby Afghans</li>
        <li>Afghans</li>
        <li>Scarves, Gloves, Hats</li>
      </ul>
    </section>
  </main>
</body>
</html>
```